Boutique Accounting firm needs a sleek, professional facebook page.

We need a facebook page, facebook logo and a template meme/add designed that we can add text to. This page a designs need to tell the client that we are professional, approachable, understand their business needs and that they can be confident that if they work with us they will get an accountant who offers expert advice and service working with them to get the best possible outcome for their business. Our firm is located ina rural area in Gippsland VIC and deals with farmers, tradespeople, small to medium business and individuals.
attached is our logo and we want the grey used and we note that it will need to be resized to ensure it stands out and can be seen clearly.
The final design should promote growth and financial security and understanding.

Examples of pages that we identify with are:
@clearbrookledgersnz
@dunmoreassociatescharteredaccountants
@halvardenterprise

Target Market(s)

small business

Industry/Entity Type

Accounting

Colors
3176b5
0792cd

Requirements
Must have
• our logo must be designed so that the words of our brand fill up the area
Nice to have
• .
Should not have
• .

```html
<!DOCTYPE html>
<html lang="en">
<head>
<meta charset="utf-8">
<title>Northvale Accounting – Facebook Page Set</title>
<link href="https://fonts.googleapis.com/css2?family=Tinos:wght@400;700&display=swap" rel="stylesheet">
<style>
  :root{
    --brand-blue:#0792cd;
    --brand-deep:#3176b5;
    --brand-navy:#1f679f;
    --panel-blue:#1d8fd0;
    --ink:#2b2b2b;
    --paper:#ffffff;
    --board:#f4f5f7;
  }
  html,body{margin:0;padding:0;}
  body{
    width:1200px;height:3000px;overflow:hidden;
    background:var(--board);position:relative;
    font-family:"Tinos","Times New Roman",serif;
  }
  .piece{position:absolute;background:var(--paper);box-shadow:0 4px 14px rgba(0,0,0,.14);overflow:hidden;}
  .piece svg{display:block;width:100%;height:100%;}
  .cover-wide{left:48px;top:40px;width:1104px;height:440px;}
  .cover-bold{left:48px;top:512px;width:1104px;height:428px;}
  .page-showcase{left:0;top:1000px;width:1200px;height:800px;background:var(--panel-blue);box-shadow:none;}
  .post{width:552px;height:540px;}
  .post-team{left:48px;top:1840px;}
  .post-call{left:600px;top:1840px;}
  .post-profile{left:48px;top:2420px;}
  .post-group{left:600px;top:2420px;}

  .headline{font-family:"Tinos","Times New Roman",serif;font-weight:700;fill:var(--paper);}
  .tagline{font-family:"Tinos","Times New Roman",serif;font-weight:400;fill:var(--paper);}
  .body-copy{font-family:"Tinos","Times New Roman",serif;font-weight:400;fill:var(--paper);}
  .firm-name{font-family:"Tinos","Times New Roman",serif;font-weight:700;fill:var(--brand-navy);}
</style>
</head>
<body>

<svg width="0" height="0" style="position:absolute">
  <defs>
    <linearGradient id="photo-office" x1="0" y1="0" x2="1" y2="1">
      <stop offset="0" stop-color="#eef1f4"/>
      <stop offset="0.55" stop-color="#b8c6d4"/>
      <stop offset="1" stop-color="#6f8aa3"/>
    </linearGradient>
    <linearGradient id="photo-desk" x1="0" y1="0" x2="1" y2="1">
      <stop offset="0" stop-color="#f3f1ee"/>
      <stop offset="0.6" stop-color="#c9cfd6"/>
      <stop offset="1" stop-color="#7d8d9d"/>
    </linearGradient>
    <linearGradient id="photo-people" x1="0" y1="0" x2="1" y2="1">
      <stop offset="0" stop-color="#efe6dc"/>
      <stop offset="0.5" stop-color="#c7b4a2"/>
      <stop offset="1" stop-color="#7b6c62"/>
    </linearGradient>
    <linearGradient id="photo-suits" x1="0" y1="0" x2="0" y2="1">
      <stop offset="0" stop-color="#e4e8ec"/>
      <stop offset="0.6" stop-color="#5d6670"/>
      <stop offset="1" stop-color="#2f353c"/>
    </linearGradient>
    <clipPath id="clip-profile"><circle cx="420" cy="330" r="190"/></clipPath>
    <clipPath id="clip-group"><circle cx="276" cy="660" r="330"/></clipPath>
  </defs>
</svg>

<!-- Cover: wide version -->
<section class="piece cover-wide">
  <svg viewBox="0 0 1104 440">
    <rect x="500" y="10" width="594" height="312" fill="url(#photo-office)" role="img" aria-label="Photo: team reviewing financial charts at a meeting table"/>
    <rect x="380" y="34" width="640" height="276" fill="none" stroke="var(--brand-blue)" stroke-width="4"/>
    <polygon points="40,96 470,96 430,226 40,226" fill="var(--brand-navy)"/>
    <text class="headline" x="66" y="160" font-size="52">Business</text>
    <text class="tagline" x="66" y="202" font-size="30">works like a magic.</text>
    <text class="firm-name" x="60" y="372" font-size="28">Northvale Accounting</text>
  </svg>
</section>

<!-- Cover: bold version -->
<section class="piece cover-bold">
  <svg viewBox="0 0 1104 428">
    <rect x="520" y="22" width="570" height="384" fill="url(#photo-desk)" role="img" aria-label="Photo: laptop with charts on an office desk"/>
    <rect x="600" y="40" width="470" height="350" fill="none" stroke="var(--brand-blue)" stroke-width="4"/>
    <path d="M0 0 H610 C540 140 580 300 470 428 H0 Z" fill="var(--brand-blue)"/>
    <circle cx="120" cy="470" r="175" fill="var(--paper)"/>
    <text class="headline" x="56" y="200" font-size="80">Business</text>
    <text class="tagline" x="56" y="262" font-size="46">works like a magic.</text>
    <text class="firm-name" x="40" y="396" font-size="24">Northvale Accounting</text>
  </svg>
</section>

<!-- Page showcase panel -->
<section class="piece page-showcase">
  <svg viewBox="0 0 1200 800">
    <circle cx="960" cy="110" r="110" fill="var(--paper)"/>
    <circle cx="1020" cy="650" r="130" fill="var(--paper)"/>
    <rect x="120" y="270" width="200" height="200" fill="none" stroke="var(--paper)" stroke-width="5"/>
    <g transform="translate(280,278)">
      <rect width="640" height="244" fill="var(--paper)"/>
      <rect x="290" y="6" width="344" height="180" fill="url(#photo-office)" role="img" aria-label="Photo: team reviewing financial charts at a meeting table"/>
      <rect x="220" y="20" width="370" height="160" fill="none" stroke="var(--brand-blue)" stroke-width="3"/>
      <polygon points="24,56 272,56 250,130 24,130" fill="var(--brand-navy)"/>
      <text class="headline" x="40" y="93" font-size="30">Business</text>
      <text class="tagline" x="40" y="118" font-size="18">works like a magic.</text>
      <text class="firm-name" x="34" y="212" font-size="17">Northvale Accounting</text>
    </g>
  </svg>
</section>

<!-- Post: team -->
<section class="piece post post-team">
  <svg viewBox="0 0 552 540">
    <rect width="552" height="540" fill="url(#photo-people)" role="img" aria-label="Photo: colleagues working together around a table"/>
    <path d="M0 330 C150 285 400 285 552 330 V540 H0 Z" fill="var(--brand-blue)"/>
    <rect x="36" y="36" width="480" height="470" fill="none" stroke="var(--paper)" stroke-width="3"/>
    <text class="headline" x="276" y="412" font-size="46" text-anchor="middle">Lorem ipsum</text>
    <text class="body-copy" x="276" y="446" font-size="18" text-anchor="middle">dolor sit amet, no falso</text>
    <text class="body-copy" x="276" y="470" font-size="18" text-anchor="middle">explicari pri, ne mei</text>
    <text class="body-copy" x="276" y="494" font-size="18" text-anchor="middle">partiendo adversarium, ei</text>
  </svg>
</section>

<!-- Post: call -->
<section class="piece post post-call">
  <svg viewBox="0 0 552 540">
    <rect x="0" y="70" width="552" height="470" fill="url(#photo-office)" role="img" aria-label="Photo: smiling support consultant wearing a headset"/>
    <rect x="360" y="90" width="170" height="400" fill="none" stroke="var(--brand-blue)" stroke-width="4"/>
    <path d="M0 300 C170 250 340 330 380 540 H0 Z" fill="var(--brand-blue)"/>
    <text class="firm-name" x="14" y="44" font-size="24">Northvale Accounting</text>
    <text class="headline" x="22" y="402" font-size="52">Give us</text>
    <text class="headline" x="22" y="456" font-size="52">a call today.</text>
    <text class="body-copy" x="22" y="488" font-size="17">Lorem dolor sit amet, no falso</text>
    <text class="body-copy" x="22" y="510" font-size="17">explicari pri, ne mei adversarium</text>
  </svg>
</section>

<!-- Post: profile -->
<section class="piece post post-profile">
  <svg viewBox="0 0 552 540">
    <rect width="552" height="540" fill="var(--paper)"/>
    <path d="M0 80 H310 C230 250 230 400 300 540 H0 Z" fill="var(--brand-blue)"/>
    <rect x="220" y="130" width="420" height="410" fill="url(#photo-suits)" clip-path="url(#clip-profile)" role="img" aria-label="Photo: smiling businessman in a suit"/>
    <text class="firm-name" x="14" y="44" font-size="24">Northvale Accounting</text>
    <text class="headline" x="28" y="300" font-size="26">DANIEL REYES</text>
    <text class="tagline" x="28" y="328" font-size="19">Digital Marketing</text>
    <text class="body-copy" x="28" y="380" font-size="16">dolor sit amet, no falso</text>
    <text class="body-copy" x="28" y="402" font-size="16">explicari pri, ne mei</text>
    <text class="body-copy" x="28" y="424" font-size="16">partiendo adversarium, ei</text>
  </svg>
</section>

<!-- Post: group -->
<section class="piece post post-group">
  <svg viewBox="0 0 552 540">
    <rect width="552" height="540" fill="var(--brand-blue)"/>
    <rect x="0" y="0" width="260" height="58" fill="var(--paper)"/>
    <text class="firm-name" x="14" y="38" font-size="24">Northvale Accounting</text>
    <text class="headline" x="300" y="92" font-size="36">Lorem ipsum</text>
    <text class="body-copy" x="300" y="122" font-size="16">dolor sit amet, no falso</text>
    <text class="body-copy" x="300" y="144" font-size="16">explicari pri, ne mei</text>
    <text class="body-copy" x="300" y="166" font-size="16">partiendo adversarium, ei</text>
    <circle cx="276" cy="660" r="344" fill="none" stroke="var(--paper)" stroke-width="4"/>
    <rect x="-60" y="320" width="680" height="240" fill="url(#photo-suits)" clip-path="url(#clip-group)" role="img" aria-label="Photo: group of business professionals standing together"/>
  </svg>
</section>

</body>
</html>
```